Trade Show Back Wall Display
10' x 8' 3-Section Banners
Project: Trade Show Back Wall Display
Trade Show Back Wall Display - Industrial Supplies
Creative Brief
Industrial Supplies
Corporate and Field Personnel.
Color scheme must be pulled from our logo, focusing on red, black and white. It is a 3 banner system used to create the back wall so attention must be paid to enclosed spec sheets. Time is a factor. Once the design process is getting close I will provide text/taglines to be inserted on the banners.

```html
<!DOCTYPE html>
<html lang="en">
<head>
<meta charset="utf-8">
<title>Harlan Supply – Trade Show Back Wall</title>
<link rel="stylesheet" href="https://fonts.googleapis.com/css2?family=Arimo:wght@400;700&display=swap">
<style>
  :root {
    --stage: #d6d6d6;
    --red: #b5141d;
    --red-deep: #7e0a10;
    --red-bright: #e0222c;
    --ink: #1b1b1b;
    --charcoal: #3a3a3a;
    --white: #ffffff;
    --mist: #eeeeee;
    --sky: #3f7fc4;
    --sky-light: #a9cdee;
    --steel: #6f7f8f;
    --steel-light: #c7d0d8;
  }
  * { box-sizing: border-box; margin: 0; padding: 0; }
  html, body { width: 1200px; height: 850px; overflow: hidden; }
  body {
    background: var(--stage);
    font-family: "Arimo", Arial, sans-serif;
    position: relative;
  }
  .back-wall {
    position: absolute;
    left: 18px;
    top: 15px;
    display: flex;
    gap: 12px;
  }
  .banner {
    position: relative;
    width: 380px;
    height: 820px;
    overflow: hidden;
    background: var(--red);
  }
  .banner-shapes { position: absolute; inset: 0; width: 380px; height: 820px; }
  .banner-photo {
    position: absolute;
    left: 0; top: 0;
    width: 380px; height: 300px;
  }
  .photo-oilfield { background: linear-gradient(170deg, var(--sky) 0%, var(--sky-light) 55%, #8a4a4a 100%); }
  .photo-industrial { background: linear-gradient(200deg, var(--steel-light) 0%, var(--steel) 60%, #3d4752 100%); }
  .brand-field {
    position: absolute;
    left: 0; top: 0;
    width: 380px; height: 300px;
    background: linear-gradient(180deg, var(--white) 0%, var(--mist) 70%, #cfcfcf 100%);
  }
  .brand-name {
    position: absolute;
    top: 92px; left: 0; width: 100%;
    display: flex; align-items: center; justify-content: center; gap: 12px;
    font-weight: 700;
    font-size: 44px;
    letter-spacing: 2px;
    color: var(--charcoal);
  }
  .brand-square { width: 34px; height: 34px; background: var(--red); }
  .banner-heading {
    position: absolute;
    top: 304px; left: 0; width: 100%;
    height: 44px;
    line-height: 44px;
    text-align: center;
    color: var(--white);
    font-weight: 700;
    font-size: 30px;
    letter-spacing: 1.5px;
  }
  .banner-copy {
    position: absolute;
    top: 378px; left: 40px; right: 40px;
    color: var(--white);
    font-size: 15px;
    line-height: 1.45;
  }
  .banner-copy p + p { margin-top: 22px; }
  .call-block {
    position: absolute;
    top: 730px; left: 0; width: 100%;
    text-align: center;
    color: var(--ink);
  }
  .call-label { font-size: 20px; letter-spacing: 2px; }
  .call-number { font-size: 30px; font-weight: 700; letter-spacing: 3px; margin-top: 2px; }
</style>
</head>
<body>
<main class="back-wall">

  <section class="banner banner-oilfield">
    <div class="banner-photo photo-oilfield" role="img" aria-label="Photo of an oilfield wellhead with red valves against a blue sky"></div>
    <svg class="banner-shapes" viewBox="0 0 380 820" aria-hidden="true">
      <defs>
        <linearGradient id="band-a" x1="0" y1="0" x2="0" y2="1"><stop offset="0" stop-color="#4a4a4a"/><stop offset="1" stop-color="#111"/></linearGradient>
        <radialGradient id="glow-a"><stop offset="0" stop-color="#e0222c"/><stop offset="1" stop-color="#e0222c" stop-opacity="0"/></radialGradient>
        <linearGradient id="foot-a" x1="0" y1="0" x2="0" y2="1"><stop offset="0" stop-color="#fff"/><stop offset="1" stop-color="#dcdcdc"/></linearGradient>
      </defs>
      <path d="M0 296 Q190 276 380 296 L380 354 Q190 342 0 354 Z" fill="url(#band-a)"/>
      <ellipse cx="190" cy="326" rx="160" ry="20" fill="url(#glow-a)"/>
      <path d="M0 664 Q190 616 380 664 L380 688 Q190 640 0 688 Z" fill="#7e0a10"/>
      <path d="M0 688 Q190 640 380 688 L380 820 L0 820 Z" fill="url(#foot-a)"/>
    </svg>
    <h2 class="banner-heading">OILFIELD</h2>
    <div class="banner-copy">
      <p>Rugged supply for every well site. We stock pipe, valves, fittings and tools that keep drilling crews working. Fast quotes, field delivery and expert staff ready to help your team.</p>
      <p>Ask about our rig service program and volume pricing for field crews.</p>
    </div>
  </section>

  <section class="banner banner-plumbing">
    <div class="brand-field">
      <div class="brand-name"><span class="brand-square"></span>HARLAN</div>
    </div>
    <svg class="banner-shapes" viewBox="0 0 380 820" aria-hidden="true">
      <defs>
        <linearGradient id="band-b" x1="0" y1="0" x2="0" y2="1"><stop offset="0" stop-color="#4a4a4a"/><stop offset="1" stop-color="#111"/></linearGradient>
        <radialGradient id="glow-b"><stop offset="0" stop-color="#e0222c"/><stop offset="1" stop-color="#e0222c" stop-opacity="0"/></radialGradient>
        <linearGradient id="foot-b" x1="0" y1="0" x2="0" y2="1"><stop offset="0" stop-color="#fff"/><stop offset="1" stop-color="#dcdcdc"/></linearGradient>
      </defs>
      <path d="M0 296 Q190 276 380 296 L380 354 Q190 342 0 354 Z" fill="url(#band-b)"/>
      <ellipse cx="190" cy="326" rx="160" ry="20" fill="url(#glow-b)"/>
      <path d="M0 664 Q190 616 380 664 L380 688 Q190 640 0 688 Z" fill="#7e0a10"/>
      <path d="M0 688 Q190 640 380 688 L380 820 L0 820 Z" fill="url(#foot-b)"/>
    </svg>
    <h2 class="banner-heading">PLUMBING</h2>
    <div class="banner-copy">
      <p>Complete plumbing supply under one roof. Copper, PVC, fixtures, valves and water heaters for contractors and builders. Same day pickup, job site delivery and counter staff who know the trade.</p>
      <p>Open early for contractors with trade accounts and fast order tracking.</p>
    </div>
    <div class="call-block">
      <div class="call-label">CALL TODAY</div>
      <div class="call-number">987.654.321</div>
    </div>
  </section>

  <section class="banner banner-industrial">
    <div class="banner-photo photo-industrial" role="img" aria-label="Photo of industrial steel piping and machinery"></div>
    <svg class="banner-shapes" viewBox="0 0 380 820" aria-hidden="true">
      <defs>
        <linearGradient id="band-c" x1="0" y1="0" x2="0" y2="1"><stop offset="0" stop-color="#4a4a4a"/><stop offset="1" stop-color="#111"/></linearGradient>
        <radialGradient id="glow-c"><stop offset="0" stop-color="#e0222c"/><stop offset="1" stop-color="#e0222c" stop-opacity="0"/></radialGradient>
        <linearGradient id="foot-c" x1="0" y1="0" x2="0" y2="1"><stop offset="0" stop-color="#fff"/><stop offset="1" stop-color="#dcdcdc"/></linearGradient>
      </defs>
      <path d="M0 296 Q190 276 380 296 L380 354 Q190 342 0 354 Z" fill="url(#band-c)"/>
      <ellipse cx="190" cy="326" rx="160" ry="20" fill="url(#glow-c)"/>
      <path d="M0 664 Q190 616 380 664 L380 688 Q190 640 0 688 Z" fill="#7e0a10"/>
      <path d="M0 688 Q190 640 380 688 L380 820 L0 820 Z" fill="url(#foot-c)"/>
    </svg>
    <h2 class="banner-heading">INDUSTRIAL</h2>
    <div class="banner-copy">
      <p>Industrial parts for plants and shops. Bearings, hose, safety gear, fasteners and power tools in stock and ready to ship. Inventory programs and skilled reps to keep your lines moving.</p>
      <p>Ask about vendor managed inventory and plant maintenance supply plans.</p>
    </div>
  </section>

</main>
</body>
</html>
```